Graphic Design Project - Coffee Label

I am a coffee roasting business and I need a professional label design for my bag of coffee. this needs to be in a format that we can change the "title" or "weight" of the product frequently ourselves. We do have photoshop, but cannot create the project, but can edit if need be to print. Our labels are 3"x8". we will want the colors to bleed to the end. The labels are white and glossy, but i want the design to give the illusion that the color of the label is not evident. I have a logo. I do not want the design to have a border. Since the label is only 3" wide and 8" tall the design needs to be creative to look good. although coffee colors are ok, I want a lot more color to not be boring. We could frequently change the label size and would need to adjust accordingly from the current design.
Updates

Project Deadline Extended
Reason: I just decided to remove my refundable contract into committed payment to a designer. I would like a few more days to broadcast that option.

Target Market(s)

30-50 year olds that have money and want to buy quality

Industry/Entity Type

Business

Requirements
Must have
• we currently are using label 3" wide and 8" tall. First and foremost I need to be able to edit the words on the label. I will need to change the net wt and the coffee blend names. I would like the ability to change the size if need be. the company name is
1. Heron Dusk Coffee
2. Artisan Coffee Roasting
3. Needs to be a large space for a particular coffee name i.e Rain, Fern and Pebble Blend. Use this blend, but I need to be able to edit it for other blends.
4. Under the blend it should say Whole Bean. Also need to be able to edit.
5. At the bottom it should say Roasted in Cedar Hollow, Texas. www.herondusk-example.com
6. Below the coffee name there should be Net Weight ie 16 oz (this also needs to be editable for us)
Nice to have
• I have a logo, but it can be different. Labels are white, but I don't want borders, and would like the colors to bleed and not to appear to be a white label. the bags are light grey/silver metallic. Although many use a lot of "coffee" colors for design, I do not. I have pics of coffee beans; it doesn't have to be used. I don't want to be just a block of a pic of beans. Other pics of coffee related ideas is fine with me. I don't need the brand to dominate the label. Bolder colors. I have attached roasting pics. These do not have to be used, but can. If used please edit out the extraneous background.
Should not have
• Do not use borders. I want the colors to bleed to the end. I don't want the white label to show through as though I have a typed page of print. I don't want just coffee colors used. I don't want light colors. I don't want a "square" looking format wherein everything is just line by line. Asymmetrical is ok.

```html
<!DOCTYPE html>
<html lang="en">
<head>
<meta charset="utf-8">
<title>Heron Dusk Coffee – Whole Bean Label</title>
<link href="https://fonts.googleapis.com/css2?family=Oswald:wght@400;500;600;700&display=swap" rel="stylesheet">
<style>
  :root {
    --page: #ffffff;
    --label-top: #e9ad2e;
    --label-mid: #eba02a;
    --label-bottom: #ec8a1e;
    --ribbon-top: #7b5733;
    --ribbon-bottom: #3a2415;
    --gold: #f2b62a;
    --tan: #c9a878;
    --espresso: #2e1a0e;
    --silver-light: #f4f4f4;
    --silver-mid: #dcdcdc;
    --silver-dark: #a9a9a9;
    --white: #ffffff;
    --badge: #f29a1c;
  }
  html, body {
    margin: 0;
    padding: 0;
    width: 1186px;
    height: 1200px;
    overflow: hidden;
    background: var(--page);
  }
  .canvas {
    position: relative;
    width: 1186px;
    height: 1200px;
  }
  .label {
    position: absolute;
    left: 404px;
    top: 91px;
    width: 385px;
    height: 1010px;
    overflow: hidden;
    font-family: 'Oswald', sans-serif;
  }
  .label__backdrop {
    position: absolute;
    inset: 0;
    background: linear-gradient(180deg, var(--label-top) 0%, var(--label-mid) 55%, var(--label-bottom) 100%);
  }
  .label__ribbon {
    position: absolute;
    left: 0;
    top: 0;
    width: 385px;
    height: 780px;
  }
  .text {
    position: absolute;
    left: 26px;
    width: 257px;
    margin: 0;
    text-align: center;
    text-transform: uppercase;
    line-height: 1;
    white-space: nowrap;
  }
  .brand-name {
    top: 118px;
    font-size: 21px;
    font-weight: 600;
    color: var(--gold);
    letter-spacing: 0.5px;
  }
  .brand-tagline {
    top: 358px;
    font-size: 16px;
    font-weight: 500;
    color: var(--gold);
  }
  .blend-name {
    left: 22px;
    width: 257px;
    top: 404px;
    height: 152px;
    display: flex;
    align-items: center;
    justify-content: center;
    font-size: 108px;
    font-weight: 700;
    color: var(--espresso);
    letter-spacing: 1px;
  }
  .bean-style {
    top: 588px;
    font-size: 16px;
    font-weight: 500;
    color: var(--tan);
  }
  .net-weight {
    left: 0;
    width: 385px;
    top: 856px;
    font-size: 40px;
    font-weight: 500;
    color: var(--espresso);
  }
  .origin {
    left: 0;
    width: 385px;
    top: 933px;
    font-size: 15px;
    font-weight: 500;
    color: var(--white);
  }
  .website {
    left: 0;
    width: 385px;
    top: 964px;
    font-size: 17px;
    font-weight: 600;
    color: var(--espresso);
    letter-spacing: 0.3px;
  }
</style>
</head>
<body>
<div class="canvas">
  <section class="label">
    <div class="label__backdrop" role="img" aria-label="Golden to orange backdrop with a faint pattern of scattered coffee beans"></div>

    <svg class="label__ribbon" viewBox="0 0 385 780" xmlns="http://www.w3.org/2000/svg" aria-hidden="true">
      <defs>
        <linearGradient id="ribbon-fill" x1="0" y1="0" x2="0" y2="1">
          <stop offset="0" stop-color="var(--ribbon-top)"/>
          <stop offset="1" stop-color="var(--ribbon-bottom)"/>
        </linearGradient>
        <linearGradient id="silver-fill" x1="0" y1="0" x2="1" y2="0">
          <stop offset="0" stop-color="var(--silver-dark)"/>
          <stop offset="0.3" stop-color="var(--silver-light)"/>
          <stop offset="0.7" stop-color="var(--silver-mid)"/>
          <stop offset="1" stop-color="var(--silver-dark)"/>
        </linearGradient>
        <filter id="ribbon-shadow" x="-10%" y="-5%" width="130%" height="115%">
          <feDropShadow dx="6" dy="4" stdDeviation="5" flood-color="#000" flood-opacity="0.35"/>
        </filter>
      </defs>

      <path class="ribbon" d="M26 0 H283 V614 L26 738 Z" fill="url(#ribbon-fill)" filter="url(#ribbon-shadow)"/>
      <path class="ribbon-stitch" d="M49 0 V700 L262 598 V0" fill="none" stroke="var(--gold)" stroke-width="2" stroke-dasharray="4 4"/>

      <circle class="brand-mark" cx="154" cy="245" r="86" fill="var(--badge)"/>

      <rect class="name-band" x="22" y="404" width="257" height="152" fill="url(#silver-fill)" filter="url(#ribbon-shadow)"/>
    </svg>

    <p class="text brand-name">Heron Dusk Coffee</p>
    <p class="text brand-tagline">Artisan Coffee Roasting</p>
    <h1 class="text blend-name">Fern</h1>
    <p class="text bean-style">Whole Bean</p>

    <p class="text net-weight">Net Wt. 16 oz</p>
    <p class="text origin">Roasted in Cedar Hollow, Texas</p>
    <p class="text website">www.herondusk-example.com</p>
  </section>
</div>
</body>
</html>
```